Brand New Upscale OOBGYN Office

Im in Need of an advertising one sided postcard as soon as possible. It's for a brand new OBGYN office in the Northern Virginia area. We are trying to create a new patient customer base. I have attached photos of the inside of the office and logos. The office contact information needs to be on the postcard. You can find that on the attached pdf file named business card. That same file is the font that needs to be used. The font is called TT Drugs. Please contact me with any questions. I would appreciated it so much if you could send me these proofs as soon as possible. Thank you!!!
Women
Advertising
- TT Drugs

```html
<!DOCTYPE html>
<html lang="en">
<head>
<meta charset="utf-8">
<title>Harbor Crest OBGYN Postcard</title>
<link rel="stylesheet" href="https://fonts.googleapis.com/css2?family=Lato:wght@300;400;700&family=Oswald:wght@500&display=swap">
<style>
  :root{
    --page:#e4e4e4;
    --pink:#f08cb2;
    --pink-deep:#d0477c;
    --green:#8cc96c;
    --green-light:#b3dc93;
    --charcoal:#333333;
    --ink:#1e1e1e;
    --grey:#7a7a7a;
    --white:#ffffff;
    --photo-warm:#c9ada1;
    --photo-soft:#e8d6cc;
    --photo-sky:#cfe6ee;
    --photo-grass:#a8cf86;
  }
  *{box-sizing:border-box;margin:0;padding:0}
  html,body{width:806px;height:1200px;overflow:hidden;background:var(--page)}
  body{font-family:"Lato",sans-serif;color:var(--ink);position:relative}
  .card{position:absolute;left:76px;width:654px;height:504px;background:var(--white);overflow:hidden;box-shadow:0 2px 6px rgba(0,0,0,.18)}
  .card--front{top:60px}
  .card--back{top:636px}
  .card__art{position:absolute;inset:0;width:100%;height:100%}

  .brand{position:absolute;left:50px;top:22px;display:flex;flex-direction:column;align-items:center;width:120px}
  .brand__dot{width:74px;height:74px;border-radius:50%;background:#8a8a8a}
  .brand__name{margin-top:10px;font-size:11px;font-weight:400;color:var(--grey);letter-spacing:.3px;white-space:nowrap}
  .brand__tag{font-size:9px;color:var(--grey);letter-spacing:.6px;white-space:nowrap}

  .headline{position:absolute;left:22px;top:202px;font-weight:300;line-height:1}
  .headline__lead{display:block;font-size:39px;color:var(--pink-deep);letter-spacing:.5px}
  .headline__mid{display:block;font-size:25px;color:var(--charcoal);margin-top:6px}
  .headline__end{display:block;font-size:31px;color:var(--pink-deep);margin-top:5px}

  .pill{position:absolute;left:0;height:27px;padding:0 28px 0 22px;background:var(--charcoal);border-radius:0 14px 14px 0;font-family:"Oswald",sans-serif;font-weight:500;font-size:17px;line-height:27px;color:var(--pink);letter-spacing:.5px}
  .pill--philosophy{top:325px}
  .pill--services{top:233px}

  .philosophy{position:absolute;left:22px;top:362px;width:300px;font-size:13.6px;line-height:17px;color:var(--ink)}

  .contact{position:absolute;left:24px;list-style:none;font-size:12.6px;font-weight:700;color:var(--ink)}
  .card--front .contact{top:438px}
  .card--back .contact{top:428px}
  .contact li{display:flex;align-items:center;height:18px}
  .contact svg{width:10px;height:10px;margin-right:7px;fill:none;stroke:var(--white);stroke-width:1.4}

  .services{position:absolute;left:24px;top:281px;list-style:none;font-size:14px;font-weight:700;line-height:17.5px}
  .services li::before{content:"";display:inline-block;width:5px;height:5px;border-radius:50%;background:var(--pink-deep);margin-right:6px;vertical-align:middle}

  .stamp{position:absolute;left:555px;top:34px;width:60px;height:76px;border:1px solid var(--charcoal)}
</style>
</head>
<body>

<section class="card card--front">
  <svg class="card__art" viewBox="0 0 610 470" preserveAspectRatio="none">
    <defs>
      <linearGradient id="greenFront" x1="0" y1="0" x2="1" y2="0">
        <stop offset="0" stop-color="var(--green)"/>
        <stop offset=".6" stop-color="var(--green-light)"/>
        <stop offset="1" stop-color="var(--green)"/>
      </linearGradient>
      <linearGradient id="photoFront" x1="0" y1="0" x2="1" y2="1">
        <stop offset="0" stop-color="var(--photo-soft)"/>
        <stop offset="1" stop-color="var(--photo-warm)"/>
      </linearGradient>
    </defs>
    <rect width="610" height="470" fill="var(--white)"/>
    <path d="M0,140 C120,175 230,160 330,110 C430,65 520,65 610,70 L610,470 L0,470 Z" fill="url(#greenFront)"/>
    <path d="M240,160 C300,120 420,78 610,72 L610,452 C520,450 400,440 340,400 C280,350 275,220 240,160 Z" fill="var(--charcoal)"/>
    <path role="img" aria-label="Photo of a mother resting beside her sleeping newborn" d="M258,162 C320,125 430,88 610,82 L610,440 C520,438 410,428 355,390 C300,345 290,220 258,162 Z" fill="url(#photoFront)"/>
    <path d="M0,112 C120,160 230,140 330,90 C420,48 520,42 610,50 L610,70 C520,62 420,72 330,115 C230,162 120,172 0,138 Z" fill="var(--pink)"/>
    <path d="M0,138 C120,172 230,162 330,115 C420,72 520,62 610,70 L610,82 C520,76 420,86 330,128 C230,176 120,182 0,150 Z" fill="var(--charcoal)"/>
    <path d="M0,398 C150,388 300,412 450,438 C520,450 580,450 610,444 L610,470 L0,470 Z" fill="var(--white)"/>
    <path d="M0,404 C150,394 300,418 450,444 C520,456 580,456 610,450 L610,470 L0,470 Z" fill="var(--pink)"/>
  </svg>

  <div class="brand">
    <span class="brand__dot"></span>
    <span class="brand__name">HARBOR CREST OBGYN</span>
    <span class="brand__tag">physicians &amp; midwives</span>
  </div>

  <h1 class="headline">
    <span class="headline__lead">CHOOSING</span>
    <span class="headline__mid">THE RIGHT OBGYN</span>
    <span class="headline__end">IS ESSENTIAL</span>
  </h1>

  <div class="pill pill--philosophy">OUR PHILOSOPHY</div>
  <p class="philosophy">When it comes to managing your health as a woman, we completely understand that it is both a private and sensitive matter.</p>

  <ul class="contact">
    <li><svg viewBox="0 0 10 10"><path d="M2,1 L4,3 L3,4 C4,6 5,7 6,7 L7,6 L9,8 L7.5,9.5 C4,9 1,6 0.5,2.5 Z"/></svg>555-014-2290</li>
    <li><svg viewBox="0 0 10 10"><rect x="0.7" y="2" width="8.6" height="6"/><path d="M0.7,2 L5,5.5 L9.3,2"/></svg>hello@harborcrestobgyn.com</li>
    <li><svg viewBox="0 0 10 10"><circle cx="5" cy="5" r="4.2"/><path d="M0.8,5 H9.2 M5,0.8 C3,3 3,7 5,9.2 M5,0.8 C7,3 7,7 5,9.2"/></svg>www.harborcrestobgyn.com</li>
  </ul>
</section>

<section class="card card--back">
  <svg class="card__art" viewBox="0 0 610 470" preserveAspectRatio="none">
    <defs>
      <linearGradient id="greenBack" x1="0" y1="0" x2="1" y2="0">
        <stop offset="0" stop-color="var(--green)"/>
        <stop offset=".55" stop-color="var(--green-light)"/>
        <stop offset="1" stop-color="var(--green)"/>
      </linearGradient>
      <linearGradient id="photoBack" x1="0" y1="0" x2="1" y2="1">
        <stop offset="0" stop-color="var(--photo-sky)"/>
        <stop offset=".5" stop-color="var(--photo-soft)"/>
        <stop offset="1" stop-color="var(--photo-grass)"/>
      </linearGradient>
    </defs>
    <rect width="610" height="470" fill="var(--white)"/>
    <path d="M0,0 L268,0 C305,40 315,110 285,170 C260,230 262,320 275,400 C282,440 290,460 295,470 L0,470 Z" fill="var(--charcoal)"/>
    <path d="M0,0 L255,0 C290,40 298,110 270,170 C245,230 248,320 260,400 C266,440 274,460 278,470 L0,470 Z" fill="var(--white)"/>
    <path d="M0,0 L248,0 C282,40 290,110 262,170 C238,230 241,320 253,400 C259,440 266,460 270,470 L0,470 Z" fill="var(--pink)"/>
    <path d="M0,0 L232,0 C266,40 274,110 248,170 C224,230 227,320 240,400 C246,440 254,460 258,470 L0,470 Z" fill="var(--white)"/>
    <path d="M0,0 L228,0 C262,40 270,110 244,170 C220,230 223,320 236,400 C242,440 250,460 254,470 L0,470 Z" fill="url(#greenBack)"/>
    <path d="M0,156 C100,168 200,150 260,95 C285,70 280,30 270,0 L0,0 Z" fill="var(--pink)"/>
    <path d="M0,148 C100,160 200,142 255,90 C278,66 274,28 264,0 L0,0 Z" fill="var(--charcoal)"/>
    <path role="img" aria-label="Photo of a smiling family of three outdoors" d="M0,0 L258,0 C266,26 270,60 250,82 C195,132 100,150 0,140 Z" fill="url(#photoBack)"/>
    <path d="M0,385 C80,378 160,385 230,398 C245,430 255,455 262,470 L0,470 Z" fill="var(--white)"/>
    <path d="M0,392 C80,385 160,392 226,405 C240,435 250,458 256,470 L0,470 Z" fill="var(--pink)"/>
  </svg>

  <div class="pill pill--services">OUR SERVICES</div>
  <ul class="services">
    <li>Obstetric and prenatal services</li>
    <li>Gynecologic services</li>
    <li>Surgical services</li>
    <li>Infertility services</li>
  </ul>

  <ul class="contact">
    <li><svg viewBox="0 0 10 10"><path d="M2,1 L4,3 L3,4 C4,6 5,7 6,7 L7,6 L9,8 L7.5,9.5 C4,9 1,6 0.5,2.5 Z"/></svg>555-014-2290</li>
    <li><svg viewBox="0 0 10 10"><rect x="0.7" y="2" width="8.6" height="6"/><path d="M0.7,2 L5,5.5 L9.3,2"/></svg>hello@harborcrestobgyn.com</li>
    <li><svg viewBox="0 0 10 10"><circle cx="5" cy="5" r="4.2"/><path d="M0.8,5 H9.2 M5,0.8 C3,3 3,7 5,9.2 M5,0.8 C7,3 7,7 5,9.2"/></svg>www.harborcrestobgyn.com</li>
  </ul>

  <div class="stamp"></div>
</section>

</body>
</html>
```